Ashcombe Homebuyers website creation

A slick professional landing page it needs to be a very engaging custom designed landing page.

It must have a lead generation tool/box similar to my competitors that will recognise the address when they start to enter the address or postcode.

My main competitors websites to use ideas from to build trust and look correct are: www.brindlecrestholdings.com quillmarshkeys.com

Target Market(s)

People looking to sell their house or property fast. We will buy their property

Industry/Entity Type

Real Estate

Coding

Coded - Design and coding required

Number of Pages Required

1 page

Requirements
Must have
• A lead generation tool that is similar to my competitors to gather their essential details. (please check www.quillmarshkeys.com or www.brindlecrestholdings.com to see what i want.

It also must have all the aspects my competitors has on their landing page. All companies in this industry have this on the landing page. These include: Logos to build trust. Ours can be The Harbinger Logo, the seen on TV logo, The Evening Quorum online logo. Also we need a step by step process map to show the customer how it works.

If the customer is about to leave the page it Must have flash ups that ask the customer to fill in 4 boxes. first name, surname, email, Phone number and address. Check out quillmarshkeys.com to see what i want.

must have a comparison table similar to my competitors. I can include this on the draft.

Must have my frequently asked questions for google SEO ( I will upload these to here to the winner to add this page at the end.

It must be a slick professional design that tells people they are dealing with a company they can trust who has the funds on hand to purchase hundreds of property.
Nice to have
• It must be a slick professional design that tells people they are dealing with a company they can trust who has the funds on hand to purchase hundreds of property.
Should not have
• Anything cheap or tacky looking.

```html
<!DOCTYPE html>
<html lang="en">
<head>
<meta charset="utf-8">
<title>Ashcombe Homebuyers – We Buy Any House For Cash</title>
<link href="https://fonts.googleapis.com/css2?family=Montserrat:ital,wght@0,400;0,500;0,600;0,700;1,400&display=swap" rel="stylesheet">
<style>
:root{
  --blue:#5b8ed8;
  --blue-dark:#4a7dcc;
  --blue-pale:#eaf0fa;
  --ink:#3a3a40;
  --muted:#8a8d96;
  --line:#e3e6ec;
  --star:#f5a623;
  --footer:#4d4c54;
  --white:#fff;
}
*{box-sizing:border-box;margin:0;padding:0}
html,body{width:1200px;height:4739px;overflow:hidden}
body{font-family:'Montserrat',sans-serif;color:var(--ink);background:var(--white);position:relative}
section,header,footer{position:absolute;left:0;width:1200px}
.center{text-align:center;left:0;width:100%}
.btn{position:absolute;background:var(--blue-dark);color:#fff;font-weight:700;font-size:13px;letter-spacing:.5px;display:flex;align-items:center;justify-content:center;border-radius:2px}
.rule{position:absolute;left:560px;width:80px;height:3px;background:var(--blue)}

/* header */
.site-header{top:0;height:88px;background:#fff;border-bottom:1px solid var(--line)}
.brand{position:absolute;display:flex;align-items:center;gap:10px;font-size:16px;font-weight:500;color:var(--ink);white-space:nowrap}
.brand-mark{width:20px;height:20px;background:var(--blue);border-radius:3px;flex:none}
.main-nav{position:absolute;left:431px;top:38px;display:flex;gap:21px;font-size:11.5px}
.main-nav .active{color:var(--blue)}
.phone-box{position:absolute;left:924px;top:28px;display:flex;gap:10px;align-items:center}
.phone-icon{width:36px;height:36px;border:1.5px solid var(--blue);border-radius:4px;display:flex;align-items:center;justify-content:center}
.phone-box small{font-size:10px;color:var(--muted);display:block}
.phone-box strong{font-size:15px;color:var(--blue);font-weight:700}

/* hero */
.hero{top:88px;height:525px;color:#fff;overflow:hidden}
.hero-photo{position:absolute;inset:0;background:linear-gradient(90deg,#2b4f8e 0%,#3d5f93 38%,#7a6d5d 62%,#a88560 82%,#8b6c50 100%)}
.hero h1{position:absolute;left:123px;top:94px;font-size:31px;font-weight:700}
.hero .lead{position:absolute;left:123px;top:143px;font-size:16.5px;line-height:27px;font-weight:500}
.hero .ask{position:absolute;left:123px;top:218px;font-size:19px;font-weight:500}
.field{position:absolute;background:#fff;border:1px solid var(--line);display:flex;align-items:center;gap:10px;padding-left:14px;font-size:12px;color:#9aa0aa}
.reviews-line{position:absolute;left:125px;top:382px;font-size:14px;font-weight:500;display:flex;gap:10px;align-items:center}
.hero .avg{position:absolute;left:123px;top:411px;font-size:11.5px}
.stars{color:var(--star);letter-spacing:1px}
.scroll-cue{position:absolute;left:578px;top:501px;width:44px;height:44px;border-radius:50%;background:#fff;display:flex;justify-content:center;padding-top:8px}

/* featured */
.featured{top:613px;height:302px}
.featured h2{position:absolute;top:74px;font-size:25px;font-weight:600}
.press{position:absolute;top:142px;width:149px;height:77px;background:#fff;box-shadow:0 2px 10px rgba(0,0,0,.08);display:flex;align-items:center;justify-content:center;font-size:15px;font-weight:700;color:#6c6c72;text-align:center}
.press .badge{width:52px;height:44px;background:#e2453c;border-radius:6px}
.arrow-nav{position:absolute;top:168px;font-size:22px;color:#9aa0aa}

/* how it works */
.how{top:915px;height:451px;background:linear-gradient(90deg,#efece7,#f6f4f1)}
.how-photo{position:absolute;left:0;top:0;width:515px;height:451px;background:linear-gradient(160deg,#8a9a7a 0%,#c9c2b4 45%,#a9413f 60%,#b9a47c 100%);clip-path:polygon(0 0,515px 0,408px 50%,515px 100%,0 100%)}
.how h2{position:absolute;left:560px;top:53px;font-size:30px;font-weight:600}
.step-icon{position:absolute;top:124px;width:88px;height:88px;border-radius:50%;background:var(--blue);border:4px solid #c8d8f2;display:flex;align-items:center;justify-content:center}
.step-arrow{position:absolute;top:155px;color:var(--blue);font-size:26px}
.step-label{position:absolute;top:231px;font-size:11.5px;line-height:19px;color:#55585f}
.how h3{position:absolute;left:560px;top:298px;font-size:23px;font-weight:700}

/* why choose */
.why{top:1366px;height:519px}
.why h2{position:absolute;top:118px;font-size:28px;font-weight:600}
.stat{position:absolute;top:202px;width:220px;text-align:center}
.stat .ring{width:74px;height:74px;border-radius:50%;background:var(--blue-pale);margin:0 auto 10px;display:flex;align-items:center;justify-content:center}
.stat b{display:block;font-size:23px;font-weight:500;margin-bottom:8px}
.stat span{font-size:11.5px;line-height:19px;display:block}
.divider-v{position:absolute;top:205px;width:1px;height:150px;background:var(--line)}

/* reviews */
.reviews{top:1885px;height:695px;background:var(--blue);color:#fff}
.reviews h2{position:absolute;top:74px;font-size:30px;font-weight:700}
.reviews .intro{position:absolute;top:143px;left:250px;width:700px;font-size:12px;line-height:19px;text-align:center}
.review-card{position:absolute;top:252px;width:307px;height:200px;background:#eef3fb;color:var(--ink);text-align:center;padding-top:62px;border-radius:2px}
.review-card.focus{background:#fff;box-shadow:0 6px 18px rgba(0,0,0,.15)}
.avatar{position:absolute;left:111px;top:-42px;width:85px;height:85px;border-radius:50%;background:linear-gradient(#d9dde4,#aeb5c2);border:3px solid #fff}
.review-card h4{font-size:14px;font-weight:500}
.review-card small{display:block;font-size:12px;color:#9aa6ba;margin:6px 0 10px}
.review-card p{font-size:11.5px;font-style:italic;line-height:20px;padding:0 30px}
.dots{position:absolute;top:489px;left:562px;display:flex;gap:6px}
.dots i{width:9px;height:9px;border-radius:50%;border:1px solid #fff}
.dots i.on{background:#fff}
.reviews .big-stars{position:absolute;top:538px;font-size:36px;letter-spacing:2px}
.reviews .score{position:absolute;top:585px;font-size:30px}

/* comparison */
.compare{top:2580px;height:792px}
.compare h2{position:absolute;top:71px;font-size:30px;font-weight:600}
.table{position:absolute;left:160px;top:157px;width:878px}
.table-head{display:grid;grid-template-columns:521px 177px 180px;height:88px}
.head-title{background:var(--blue);color:#fff;font-weight:700;font-size:19px;display:flex;align-items:flex-end;padding:0 0 14px 33px}
.head-col{display:grid;grid-template-rows:44px 44px;text-align:center}
.head-col span{background:#bcd0ef;color:#4a5872;font-size:12px;display:flex;align-items:center;justify-content:center;border-right:1px solid #fff}
.head-col strong{background:var(--blue-dark);color:#fff;font-size:20px;display:flex;align-items:center;justify-content:center}
.row{display:grid;grid-template-columns:521px 177px 180px;height:44px;font-size:12.5px;align-items:center}
.row:nth-child(even){background:var(--blue-pale)}
.row div:first-child{padding-left:31px;line-height:22px}
.row div:not(:first-child){text-align:center}
.row.tall{height:70px}
.total{display:grid;grid-template-columns:521px 177px 180px}
.total span{background:var(--blue);color:#fff;font-size:12px;height:46px;display:flex;align-items:center;justify-content:center;border-right:1px solid #fff}
.total strong{background:#4a4a4f;color:#fff;font-size:22px;height:45px;display:flex;align-items:center;justify-content:center;font-weight:600}

/* cta */
.cta{top:3372px;height:294px;color:#fff;text-align:center}
.cta-photo{position:absolute;inset:0;background:linear-gradient(180deg,#5c8fd8,#6b95d3 60%,#5784cc)}
.cta h2{position:absolute;top:67px;font-size:30px;line-height:44px;font-weight:700}
.cta .btn{left:532px;top:180px;width:132px;height:38px;background:#e9ecf2;color:var(--ink)}

/* faq */
.faq-band{top:4169px;height:570px;background:var(--footer)}
.faq{top:3740px;left:160px;width:878px;height:622px;background:#fff;box-shadow:0 6px 24px rgba(0,0,0,.14)}
.faq::after{content:"";position:absolute;left:12px;right:12px;bottom:-8px;height:8px;background:#e6e8ee}
.faq h2{position:absolute;top:78px;font-size:30px;font-weight:600}
.acc{position:absolute;left:90px;width:735px;height:32px;background:var(--blue-pale);display:flex;align-items:center;justify-content:space-between;padding:0 14px;font-size:11.5px}
.acc.open{background:var(--blue);color:#fff}
.acc i{width:17px;height:17px;border-radius:50%;background:var(--blue);color:#fff;font-style:normal;font-size:14px;display:flex;align-items:center;justify-content:center}
.acc.open i{background:#fff;color:var(--blue)}
.acc-body{position:absolute;left:90px;top:194px;width:735px;height:93px;background:#fff;box-shadow:0 2px 8px rgba(0,0,0,.08);font-size:11.5px;line-height:25px;padding:11px 14px}

/* footer */
.site-footer{top:4362px;height:377px;color:#e8e8ec;font-size:11px}
.site-footer .brand{left:123px;top:96px;color:#fff;font-size:16px}
.site-footer .brand-mark{background:#fff}
.footer-about{position:absolute;left:124px;top:155px;width:210px;line-height:19px;font-size:11.5px}
.footer-title{position:absolute;top:60px;font-size:14px;font-weight:600;color:#fff}
.link{position:absolute;font-size:11px}
.ring-ic{position:absolute;width:36px;height:36px;border:1.5px solid #fff;border-radius:50%;display:flex;align-items:center;justify-content:center}
.contact{position:absolute;line-height:19px;font-size:11px}
.contact b{font-weight:600;color:#fff}
.privacy{position:absolute;left:353px;top:217px;width:720px;line-height:19px;font-size:10px}
.footer-rule{position:absolute;left:160px;top:313px;width:878px;height:1px;background:#65646c}
.copyright{position:absolute;top:342px;font-size:11.5px}
</style>
</head>
<body>

<header class="site-header">
  <div class="brand" style="left:123px;top:33px">
    <span class="brand-mark"></span>
    <span>Ashcombe Homebuyers</span>
  </div>
  <nav class="main-nav">
    <span class="active">Home</span><span>How it Works</span><span>Sell Property Fast</span><span>Value My House</span><span>About Us</span>
  </nav>
  <div class="phone-box">
    <div class="phone-icon"><svg width="18" height="18" viewBox="0 0 24 24" fill="none" stroke="#5b8ed8" stroke-width="2"><path d="M5 3h4l2 5-3 2a11 11 0 0 0 6 6l2-3 5 2v4a2 2 0 0 1-2 2A17 17 0 0 1 3 5a2 2 0 0 1 2-2z"/></svg></div>
    <div><small>Call Us Today</small><strong>123 456 7890</strong></div>
  </div>
</header>

<section class="hero">
  <div class="hero-photo" role="img" aria-label="City skyline with historic spires and rooftops at sunset, tinted blue on the left"></div>
  <h1>We Buy Any House For Cash</h1>
  <p class="lead">We Can Buy Your Property For Cash Have Your<br>Money In As Little As Two Weeks</p>
  <p class="ask">Find Out How Much You Can Get</p>
  <div class="field" style="left:123px;top:258px;width:413px;height:46px">
    <svg width="14" height="18" viewBox="0 0 14 18"><path d="M7 0a7 7 0 0 0-7 7c0 5 7 11 7 11s7-6 7-11a7 7 0 0 0-7-7z" fill="#5b8ed8"/><circle cx="7" cy="7" r="2.5" fill="#fff"/></svg>
    Enter Your Postcode
  </div>
  <div class="btn" style="left:123px;top:324px;width:137px;height:39px">GET AN OFFER</div>
  <div class="reviews-line">REVIEWS <span class="stars">★★★★★</span></div>
  <p class="avg">4.89 Average | 531 Reviews</p>
  <div class="scroll-cue"><svg width="16" height="10" viewBox="0 0 16 10"><path d="M2 2l6 6 6-6" stroke="#5b8ed8" stroke-width="2" fill="none"/></svg></div>
</section>

<section class="featured">
  <h2 class="center">As Featured On</h2>
  <span class="arrow-nav" style="left:137px">‹</span>
  <div class="press" style="left:160px">Glasswell Post</div>
  <div class="press" style="left:340px">The Harbinger</div>
  <div class="press" style="left:525px"><span class="badge"></span></div>
  <div class="press" style="left:705px">Transit Daily</div>
  <div class="press" style="left:887px">Northvale TV</div>
  <span class="arrow-nav" style="left:1054px">›</span>
</section>

<section class="how">
  <div class="how-photo" role="img" aria-label="White clapboard house with red door and autumn tree"></div>
  <h2>How It Works</h2>
  <div class="step-icon" style="left:560px"><svg width="34" height="40" viewBox="0 0 34 40" fill="none" stroke="#fff" stroke-width="2"><rect x="3" y="3" width="28" height="34" rx="2"/><path d="M9 12h16M9 18h16M9 24h10"/></svg></div>
  <span class="step-arrow" style="left:684px">›</span>
  <div class="step-icon" style="left:740px"><svg width="40" height="40" viewBox="0 0 40 40" fill="none" stroke="#fff" stroke-width="2"><circle cx="18" cy="20" r="14"/><path d="M18 11v9l6 4"/></svg></div>
  <span class="step-arrow" style="left:866px">›</span>
  <div class="step-icon" style="left:922px"><svg width="42" height="36" viewBox="0 0 42 36" fill="none" stroke="#fff" stroke-width="2"><rect x="4" y="6" width="34" height="22" rx="2"/><circle cx="21" cy="17" r="5"/></svg></div>
  <p class="step-label" style="left:560px">Request Your<br>Free Valuation</p>
  <p class="step-label" style="left:740px">Receive Your Cash<br>Offer In 1 Hour</p>
  <p class="step-label" style="left:922px">Once Agreed Your Cash<br>Sale Is Guaranteed</p>
  <h3>Start With A Free Cash Offer...</h3>
  <div class="field" style="left:560px;top:349px;width:263px;height:43px">
    <svg width="11" height="14" viewBox="0 0 14 18"><path d="M7 0a7 7 0 0 0-7 7c0 5 7 11 7 11s7-6 7-11a7 7 0 0 0-7-7z" fill="#5b8ed8"/></svg>
    Enter your Address or postcode
  </div>
  <div class="btn" style="left:823px;top:349px;width:151px;height:43px">GET AN OFFER</div>
</section>

<section class="why">
  <h2 class="center">Why Choose Ashcombe?</h2>
  <div class="rule" style="top:168px"></div>
  <div class="stat" style="left:126px"><div class="ring"><svg width="32" height="32" viewBox="0 0 32 32" fill="none" stroke="#3a3a40" stroke-width="1.8"><rect x="3" y="6" width="26" height="23" rx="2"/><path d="M3 12h26M10 3v6M22 3v6"/></svg></div><b>1993</b><span>Operating Since 1993</span></div>
  <div class="divider-v" style="left:358px"></div>
  <div class="stat" style="left:370px"><div class="ring"><svg width="32" height="32" viewBox="0 0 32 32" fill="none" stroke="#3a3a40" stroke-width="1.8"><path d="M4 15 16 5l12 10M7 13v15h18V13M13 28v-8h6v8"/></svg></div><b>6,000</b><span>We Have Bought More Than<br>6,000 Properties</span></div>
  <div class="divider-v" style="left:602px"></div>
  <div class="stat" style="left:615px"><div class="ring"><svg width="32" height="32" viewBox="0 0 32 32" fill="none" stroke="#3a3a40" stroke-width="1.8"><circle cx="16" cy="16" r="12"/><path d="M16 9v7l5 3"/></svg></div><b>Timescales</b><span>You Are In Complete<br>Control</span></div>
  <div class="divider-v" style="left:847px"></div>
  <div class="stat" style="left:860px"><div class="ring"><svg width="32" height="32" viewBox="0 0 32 32" fill="none" stroke="#3a3a40" stroke-width="1.8"><circle cx="16" cy="16" r="12"/><path d="M19 11a3 3 0 0 0-6 1v9M11 17h6M11 22h10"/></svg></div><b>£34.2 m</b><span>Our Current Annual<br>Turnover</span></div>
  <div class="btn" style="left:532px;top:404px;width:136px;height:40px">GET AN OFFER</div>
</section>

<section class="reviews">
  <h2 class="center">Customer Reviews</h2>
  <p class="intro">Lorem ipsum dolor sit amet, consectetuer adipiscing elit, sed diam nonummy nibh euismod tincidunt ut laoreet dolore magna aliquam erat volutpat. Ut wisi enim ad minim veniam quis nostrud exerci .</p>
  <div class="review-card" style="left:131px"><div class="avatar" role="img" aria-label="Customer portrait"></div><h4>Mr Lorems</h4><small>Lorem Ipsum</small><p>" Lorem ipsum dolor sit amet, consectetuer adipiscing elit, sed diam nonummy nibh euismod tincidunt nonummy "</p></div>
  <div class="review-card focus" style="left:451px"><div class="avatar" role="img" aria-label="Customer portrait"></div><h4>Ms Maren Holt</h4><small>Lorem Ipsum</small><p>" Lorem ipsum dolor sit amet, consectetuer adipiscing elit, sed diam nonummy nibh euismod tincidunt nonummy "</p></div>
  <div class="review-card" style="left:769px"><div class="avatar" role="img" aria-label="Customer portrait"></div><h4>Mr Legister</h4><small>Lorem Ipsum</small><p>" Lorem ipsum dolor sit amet, consectetuer adipiscing elit, sed diam nonummy nibh euismod tincidunt nonummy "</p></div>
  <div class="dots"><i></i><i></i><i class="on"></i><i></i><i></i></div>
  <div class="big-stars center stars">★★★★★</div>
  <p class="score center">4.89 out of 5</p>
</section>

<section class="compare">
  <h2 class="center">Comparison Table</h2>
  <div class="rule" style="top:122px"></div>
  <div class="table">
    <div class="table-head">
      <div class="head-title">Sale Process</div>
      <div class="head-col"><span>Estate Agent</span><strong>9 Months</strong></div>
      <div class="head-col"><span>Our Service</span><strong>7 Days</strong></div>
    </div>
    <div class="rows">
      <div class="row"><div>Market value (Advertised Price)</div><div>£100,000</div><div>£80,000</div></div>
      <div class="row"><div>Offer Accepted (Typical 5% Discount)</div><div>£95,000</div><div>£80,000</div></div>
      <div class="row"><div>Post survey negotiation</div><div>£92,500</div><div>£80,000</div></div>
      <div class="row"><div>Estate agent (£92,500 @ 2% + VAT)</div><div>£90,280</div><div>£80,000</div></div>
      <div class="row"><div>Solicitor Fees (£1000 + VAT = £1200)</div><div>£89,080</div><div>£80,000</div></div>
      <div class="row tall"><div>Mortgage payments (£75K repayment @ 5%<br>PA = £563pcm or £5067 for 9 Months)</div><div>£84,017</div><div>£80,000</div></div>
      <div class="row"><div>Utility bills and Council Tax (£375 x 9 months)</div><div>£80,642</div><div>£80,000</div></div>
      <div class="row"><div>Property Clearance (Skip &amp; Deep Clean @£750)</div><div>£79,892</div><div>£80,000</div></div>
    </div>
    <div class="total">
      <div></div>
      <div><span>Final Price</span><strong>£79,892</strong></div>
      <div><span>Final Price</span><strong>£80,000</strong></div>
    </div>
  </div>
</section>

<section class="cta">
  <div class="cta-photo" role="img" aria-label="Brick house front, tinted blue"></div>
  <h2 class="center">Fill In The Form And Within 15 Seconds You Will<br>Be Pleasantly Surprised With Our Cash Offer</h2>
  <div class="btn">GET AN OFFER</div>
</section>

<section class="faq-band"></section>

<section class="faq">
  <h2 class="center">Frequently Asked Questions</h2>
  <div class="acc open" style="top:162px">How much will you offer me?<i>–</i></div>
  <div class="acc-body">Lorem ipsum dolor sit amet, consectetuer adipiscing elit, sed diam nonummy nibh euismod tincidunt ut<br>laoreet dolore magna aliquam erat volutpat. Ut wisi enim ad minim veniam.</div>
  <div class="acc" style="top:322px">Does anybody have to know about this sale?<i>+</i></div>
  <div class="acc" style="top:368px">Do I need to complete lots of paperwork?<i>+</i></div>
  <div class="acc" style="top:416px">Do I need to complete lots of paperwork?<i>+</i></div>
  <div class="acc" style="top:464px">What if I don't want to proceed?<i>+</i></div>
  <div class="acc" style="top:512px">What if I don't want to move out quickly?<i>+</i></div>
</section>

<footer class="site-footer">
  <div class="brand"><span class="brand-mark"></span><span>Ashcombe Homebuyers</span></div>
  <p class="footer-about">ASHCOMBE REAL ESTATE is the UK's No. 1 Property Buyer since 1993</p>
  <p class="footer-title" style="left:353px">Useful Links</p>
  <span class="link" style="left:353px;top:106px">• Home</span>
  <span class="link" style="left:353px;top:137px">• How it Works</span>
  <span class="link" style="left:353px;top:167px">• Sell Property Fast</span>
  <span class="link" style="left:484px;top:106px">• Value My House</span>
  <span class="link" style="left:484px;top:137px">• About Us</span>
  <span class="link" style="left:484px;top:167px">• Contact Us</span>
  <p class="footer-title" style="left:611px">Contact Details</p>
  <div class="ring-ic" style="left:608px;top:105px"><svg width="12" height="16" viewBox="0 0 14 18"><path d="M7 1a6 6 0 0 0-6 6c0 4.5 6 10 6 10s6-5.5 6-10a6 6 0 0 0-6-6z" fill="none" stroke="#fff" stroke-width="1.6"/></svg></div>
  <p class="contact" style="left:657px;top:104px"><b>ASHCOMBE</b><br>123/33 building Name, Street<br>Name, City Name, State Name<br>XY 123456, UK</p>
  <div class="ring-ic" style="left:880px;top:105px"><svg width="15" height="15" viewBox="0 0 24 24" fill="none" stroke="#fff" stroke-width="2"><path d="M5 3h4l2 5-3 2a11 11 0 0 0 6 6l2-3 5 2v4a2 2 0 0 1-2 2A17 17 0 0 1 3 5a2 2 0 0 1 2-2z"/></svg></div>
  <p class="contact" style="left:928px;top:104px"><b>Call Us Today</b><br><span style="font-size:13px">123 456 7890</span><br><span style="font-size:10px;padding-left:2px">7 Days a Week (8am-8pm)</span></p>
  <p class="privacy"><b>Privacy Policy:</b> Lorem ipsum dolor sit amet, consectetuer adipiscing elit, sed diam nonummy nibh euismod tincidunt ut laoreet dolore magna aliquam erat volutpat. Ut wisi enim ad minim veniam, quis nostrud exerci tation.</p>
  <div class="footer-rule"></div>
  <p class="copyright center">Copyright © 2020 <b>Ashcombe Homebuyers</b>. All Rights Reserved.</p>
</footer>

</body>
</html>
```